Website design for lighting products company

We want a design for our website. The website is for a company that sells lighting products. The structure is similar to the below website. We really like their design as well: www.bramleyhollowlamps.com

Industry/Entity Type

Lighting

Number of Pages Required

5+ page

Colors

Designer to choose colors to be used in the design.

Requirements
Must have
• Simple design

```html
<!DOCTYPE html>
<html lang="en">
<head>
<meta charset="utf-8">
<title>Lighting Company</title>
<link href="https://fonts.googleapis.com/css2?family=Poppins:wght@300;400;500;600;700&display=swap" rel="stylesheet">
<style>
:root{
  --ink:#1b1b1b;
  --text:#555;
  --muted:#888;
  --mint:#cfe7e3;
  --mint-deep:#d4eae5;
  --peach:#f6c9b7;
  --pink-band:#fdd6d3;
  --panel:#f4f4f4;
  --line:#e4e4e4;
  --footer:#f7f7f7;
  --base:#ebebeb;
  --star:#f2a33a;
}
*{box-sizing:border-box;margin:0;padding:0}
html,body{width:1200px;height:3000px;overflow:hidden}
body{position:relative;background:#fff;font-family:'Poppins',sans-serif;color:var(--ink)}
.abs{position:absolute}
a{color:inherit;text-decoration:none}

/* top bar */
.topbar{left:0;top:0;width:1200px;height:31px;background:#f6f6f6;border-bottom:1px solid #ececec}
.topbar .links{right:345px;top:9px;display:flex;gap:24px;font-size:8px;color:#555;letter-spacing:.3px}
.topbar .phone{left:850px;top:7px;font-size:11px;font-weight:600;color:#444;display:flex;align-items:center;gap:6px}
.topbar .search{left:950px;top:6px;width:18px;height:18px;border-radius:50%;background:var(--peach);display:flex;align-items:center;justify-content:center}

/* header */
.header{left:0;top:31px;width:1200px;height:59px;border-bottom:1px solid #eee}
.brand{font-size:16px;font-weight:600;letter-spacing:.6px;color:var(--ink)}
.header .brand{left:234px;top:19px}
.nav{right:235px;top:24px;display:flex;gap:0;font-size:10px;font-weight:500;color:#333}
.nav span{padding:0 11px;border-left:1px solid #ddd}
.nav span:first-child{border-left:none}

/* hero */
.hero{left:0;top:90px;width:1200px;height:516px;background:var(--mint)}
.play{left:234px;top:139px;width:44px;height:44px;border-radius:50%;background:var(--ink)}
.hero .welcome{left:233px;top:199px;font-size:15px;font-weight:300;color:#222}
.hero .title{left:233px;top:222px;font-size:25px;font-weight:600;letter-spacing:.6px}
.hero .tagline{left:234px;top:272px;font-size:12px;color:#222}
.btn-dark{background:var(--ink);color:#fff;font-size:12px;font-weight:600;display:flex;align-items:center;justify-content:center}
.hero .btn-dark{left:234px;top:315px;width:132px;height:36px}
.lamp{border-radius:4px}
.arrow-box{width:57px;height:53px;background:#fff;display:flex;align-items:center;justify-content:center}

/* section titles */
.sec-title{width:1200px;left:0;text-align:center;font-size:20px;font-weight:600;letter-spacing:.3px}
.rule{width:38px;height:3px;background:var(--peach);left:581px}
.plus-link{font-size:9px;font-weight:600;color:var(--ink);background:linear-gradient(transparent 60%,var(--peach) 60%);padding:0 4px}

/* brochures */
.brochures{left:233px;top:652px;width:734px;height:277px;background:var(--panel);border:1px solid var(--line)}
.bro-item{top:104px;width:220px;height:125px}
.bro-cover{left:26px;top:0;width:79px;height:121px;background:linear-gradient(160deg,#3a2f28 0%,#eef2ea 30%,#d7e6d0 60%,#5aa83a 100%);box-shadow:0 1px 3px rgba(0,0,0,.2)}
.bro-text{left:117px;top:5px;width:100px}
.bro-text h4{font-size:11.5px;font-weight:500;line-height:15px}
.bro-text p{font-size:9px;color:#444;line-height:15px;margin-top:6px}
.bro-text .plus-link{display:inline-block;margin-top:6px}
.bro-sep{top:114px;width:1px;height:100px;background:#e2e2e2}
.pager{left:565px;top:915px;width:69px;height:27px;border-radius:14px;background:#e6e6e6;display:flex;align-items:center;justify-content:center;gap:4px}
.pager i{width:6px;height:6px;border-radius:50%;background:#bbb;display:block}
.pager i:first-child{background:#666}

/* welcome */
.intro-block{left:247px;top:1092px;width:238px;height:250px;background:var(--mint-deep)}
.intro-photo{left:273px;top:1029px;width:263px;height:278px;background:radial-gradient(circle at 50% 30%,#b56a2c 0%,#4a2e1e 45%,#1a1410 100%)}
.intro-copy{left:590px;top:1045px;width:376px}
.intro-copy h2{font-size:20px;font-weight:600}
.intro-copy .rule{position:static;margin:12px 0 22px}
.intro-copy p{font-size:10.5px;line-height:16.3px;color:#555;text-align:justify;margin-bottom:16px}

/* gallery */
.tile{width:169px;height:156px}
.tile-label{left:9px;top:9px;width:151px;height:138px;background:rgba(248,200,186,.9);display:flex;align-items:center;justify-content:center;font-size:15px;color:#222}

/* products */
.product{width:170px;height:189px;background:#f6f6f6;border:1px solid #e8e8e8}
.product .shape{position:absolute}
.product .view{left:0;bottom:0;width:100%;height:38px;background:var(--ink);color:#fff;font-size:9px;font-weight:600;display:flex;align-items:center;justify-content:center}
.pname{width:170px;text-align:center;font-size:10.5px;font-weight:500;color:#222}

/* subscribe */
.subscribe{left:0;top:2495px;width:1200px;height:155px;background:var(--pink-band)}
.subscribe h3{left:282px;top:72px;font-size:17px;font-weight:600}
.subscribe .field{left:577px;top:63px;width:231px;height:34px;background:#fff;border:1px solid #eed;font-size:9.5px;color:#888;padding:10px 12px}
.subscribe .btn-dark{left:827px;top:63px;width:92px;height:34px;font-size:9.5px}

/* footer */
.footer{left:0;top:2650px;width:1200px;height:303px;background:var(--footer)}
.fcol{top:52px}
.fcol h5{font-size:9px;font-weight:600;letter-spacing:.2px;margin-bottom:16px}
.fcol ul{list-style:none;font-size:9.5px;color:#555;line-height:19px}
.contact-line{display:flex;gap:9px;font-size:9.5px;color:#555;line-height:13px;margin-bottom:13px}
.reviews{top:197px;font-size:8.5px;color:#444}
.stars{color:var(--star);font-size:11px;letter-spacing:3px}
.social{top:230px;display:flex;gap:7px}
.social i{display:block;width:26px;height:26px;border-radius:50%;border:1.5px solid #555}
.base{left:0;top:2953px;width:1200px;height:47px;background:var(--base);text-align:center;font-size:9.5px;color:#555;line-height:47px}
</style>
</head>
<body>

<!-- top utility bar -->
<div class="abs topbar">
  <div class="abs links"><span>ABOUT</span><span>NEWS</span><span>CAREERS</span><span>CONTACT</span></div>
  <div class="abs phone">
    <svg width="11" height="11" viewBox="0 0 24 24"><path d="M6.6 10.8a15 15 0 006.6 6.6l2.2-2.2c.3-.3.7-.4 1-.2 1.1.4 2.3.6 3.6.6.6 0 1 .4 1 1V20c0 .6-.4 1-1 1C10.6 21 3 13.4 3 4c0-.6.4-1 1-1h3.5c.6 0 1 .4 1 1 0 1.3.2 2.5.6 3.6.1.3 0 .7-.2 1z" fill="none" stroke="#777" stroke-width="1.6"/></svg>
    555-310-4471
  </div>
  <div class="abs search"><svg width="9" height="9" viewBox="0 0 24 24"><circle cx="10" cy="10" r="6" fill="none" stroke="#333" stroke-width="2.5"/><path d="M15 15l6 6" stroke="#333" stroke-width="2.5"/></svg></div>
</div>

<!-- header -->
<div class="abs header">
  <div class="abs brand">LIGHTING COMPANY</div>
  <nav class="abs nav"><span>PRODUCTS ⌄</span><span>SOLUTIONS ⌄</span><span>CASE STUDIES</span><span>DOWNLOADS</span></nav>
</div>

<!-- hero -->
<section class="abs hero">
  <div class="abs play"><svg width="44" height="44" viewBox="0 0 44 44"><path d="M18 14l12 8-12 8z" fill="#fff"/></svg></div>
  <div class="abs welcome">WELCOME TO</div>
  <div class="abs title brand" style="font-size:25px">LIGHTING COMPANY</div>
  <div class="abs tagline">Largest Manufacturers of Commercial Lighting Solutions</div>
  <div class="abs btn-dark">LEARN MORE</div>
  <div class="abs lamp" role="img" aria-label="Black and wood pendant lamp hanging on a cord" style="left:575px;top:0;width:185px;height:405px;background:linear-gradient(180deg,rgba(30,30,30,.0) 0%,rgba(30,30,30,.08) 50%,#2a2622 62%,#b98d5e 85%,#c79d6a 100%)"></div>
  <div class="abs lamp" role="img" aria-label="White and wood pendant lamp hanging on a cord" style="left:802px;top:0;width:164px;height:280px;background:linear-gradient(180deg,rgba(255,255,255,0) 0%,rgba(255,255,255,.25) 40%,#fbfbfb 55%,#e8e8e8 72%,#c89c67 85%,#b88a55 100%)"></div>
  <div class="abs arrow-box" style="left:0;top:463px"><svg width="14" height="20" viewBox="0 0 14 20"><path d="M11 2L3 10l8 8" fill="none" stroke="#aaa" stroke-width="2"/></svg></div>
  <div class="abs arrow-box" style="left:1143px;top:463px"><svg width="14" height="20" viewBox="0 0 14 20"><path d="M3 2l8 8-8 8" fill="none" stroke="#aaa" stroke-width="2"/></svg></div>
</section>

<!-- brochures -->
<section class="abs brochures">
  <h2 class="abs sec-title" style="width:732px;top:33px">LATEST LIGHTING COMPANY BROCHURES</h2>
  <div class="abs rule" style="left:347px;top:66px"></div>
  <div class="abs bro-item" style="left:0">
    <div class="abs bro-cover" role="img" aria-label="Brochure cover showing a street light fixture"></div>
    <div class="abs bro-text"><h4>Pellentesque habitant morbi</h4><p>Phasellus lobortis dictum orci, nec rhoncus leo sodales vehicula.</p><span class="plus-link">+ VIEW NOW</span></div>
  </div>
  <div class="abs bro-sep" style="left:244px"></div>
  <div class="abs bro-item" style="left:240px">
    <div class="abs bro-cover" role="img" aria-label="Brochure cover showing a street light fixture"></div>
    <div class="abs bro-text"><h4>Pellentesque habitant morbi</h4><p>Phasellus lobortis dictum orci, nec rhoncus leo sodales vehicula.</p><span class="plus-link">+ VIEW NOW</span></div>
  </div>
  <div class="abs bro-sep" style="left:484px"></div>
  <div class="abs bro-item" style="left:480px">
    <div class="abs bro-cover" role="img" aria-label="Brochure cover showing a street light fixture"></div>
    <div class="abs bro-text"><h4>Pellentesque habitant morbi</h4><p>Phasellus lobortis dictum orci, nec rhoncus leo sodales vehicula.</p><span class="plus-link">+ VIEW NOW</span></div>
  </div>
</section>
<div class="abs pager"><i></i><i></i><i></i><i></i></div>

<!-- welcome -->
<div class="abs intro-block"></div>
<div class="abs intro-photo" role="img" aria-label="Blurred evening street with warm hanging lights"></div>
<section class="abs intro-copy">
  <h2>WELCOME TO LIGHTING COMPANY</h2>
  <div class="rule"></div>
  <p>Lorem ipsum dolor sit amet, consectetur adipiscing elit. Vestibulum blandit lacinia tempor. Integer consequat pretium lobortis. Sed sem tortor, pharetra suscipit massa nec, placerat ultricies lacus. Fusce fringilla enim quam, vel porttitor turpis mattis eu. Nullam vitae eros ut diam viverra dictum. Donec sodales pretium tortor, eu ultricies tellus rutrum a. Vestibulum a libero sit amet arcu viverra mattis quis sit amet diam.</p>
  <p>Nullam vitae ex metus. Phasellus sed feugiat mi. Nullam id eleifend tellus. Interdum et malesuada fames ac ante ipsum primis in faucibus. Class aptent taciti sociosqu ad litora torquent per conubia nostra, per inceptos himenaeos.</p>
  <span class="plus-link">+ READ MORE</span>
</section>

<!-- application gallery -->
<div class="abs tile" style="left:234px;top:1425px;background:linear-gradient(135deg,#7a3a36,#c64040)" role="img" aria-label="Education lecture hall interior">
  <div class="abs tile-label">Education</div>
</div>
<div class="abs tile" style="left:422px;top:1425px;background:linear-gradient(180deg,#f2f2f2,#d9d9d9)" role="img" aria-label="White office with linear ceiling lights"></div>
<div class="abs tile" style="left:609px;top:1425px;background:linear-gradient(180deg,#e0604f 0%,#b8b8b8 40%,#eeeeee 100%)" role="img" aria-label="Long shopping corridor with red ceiling"></div>
<div class="abs tile" style="left:797px;top:1425px;background:linear-gradient(180deg,#e8ecef 0%,#9aa0a6 60%,#8a7a6a 100%)" role="img" aria-label="Lounge with bean bags and tree stump tables"></div>
<div class="abs tile" style="left:234px;top:1600px;background:linear-gradient(180deg,#2a5fa8,#9cc4ec)" role="img" aria-label="Blue glass office corridor"></div>
<div class="abs tile" style="left:422px;top:1600px;background:linear-gradient(180deg,#efe9e0 0%,#c9a45a 45%,#2c4a56 100%)" role="img" aria-label="Crystal chandelier in a living room"></div>
<div class="abs tile" style="left:609px;top:1600px;background:linear-gradient(180deg,#f5f3ee,#c9c4bb)" role="img" aria-label="Ring ceiling light in a modern room"></div>
<div class="abs tile" style="left:797px;top:1600px;background:linear-gradient(180deg,#3a3a32 0%,#6e6a52 50%,#2a2a26 100%)" role="img" aria-label="Street lights on a road at night"></div>

<!-- product range -->
<h2 class="abs sec-title" style="top:1820px">AN EXTENSIVE PRODUCT RANGE</h2>
<div class="abs rule" style="top:1855px"></div>

<div class="abs product" style="left:234px;top:1901px">
  <svg class="shape" width="170" height="150" viewBox="0 0 170 150"><path d="M20 40l20-10 100 110-20 5z" fill="#e2e2e2" stroke="#c4c4c4"/></svg>
  <div class="abs view">+ VIEW NOW</div>
</div>
<div class="abs product" style="left:422px;top:1901px"><svg class="shape" width="170" height="189" viewBox="0 0 170 189"><path d="M0 0l14 0 130 90 0 12-144 14v-10l130-14L0 14z" fill="#6a6a6a"/></svg></div>
<div class="abs product" style="left:609px;top:1901px"><svg class="shape" width="170" height="189" viewBox="0 0 170 189"><rect x="60" y="30" width="52" height="158" fill="#e8e8e8" stroke="#b8b8b8"/><rect x="60" y="30" width="52" height="22" fill="#777"/></svg></div>
<div class="abs product" style="left:797px;top:1901px"><svg class="shape" width="170" height="189" viewBox="0 0 170 189"><path d="M22 60l12-8 132 120-8 8z" fill="#ededed" stroke="#cfcfcf"/></svg></div>
<div class="abs pname" style="left:234px;top:2105px">Skyline Duo</div>
<div class="abs pname" style="left:422px;top:2105px">Boulevard Surface</div>
<div class="abs pname" style="left:609px;top:2105px">Boulevard Suspended</div>
<div class="abs pname" style="left:797px;top:2105px">Boulevard Recessed</div>

<div class="abs product" style="left:234px;top:2149px"><svg class="shape" width="170" height="189" viewBox="0 0 170 189"><path d="M28 58l12-8 108 90-6 12z" fill="#f4f4f4" stroke="#cfcfcf"/></svg></div>
<div class="abs product" style="left:422px;top:2149px"><svg class="shape" width="170" height="189" viewBox="0 0 170 189"><path d="M14 100l62-40 80 32-62 42z" fill="#fafafa" stroke="#ddd"/></svg></div>
<div class="abs product" style="left:609px;top:2149px"><svg class="shape" width="170" height="189" viewBox="0 0 170 189"><path d="M22 60l16-8 110 96-16 8z" fill="#f7f7f7" stroke="#c8c8c8"/></svg></div>
<div class="abs product" style="left:797px;top:2149px"><svg class="shape" width="170" height="189" viewBox="0 0 170 189"><path d="M48 60h74v44a37 12 0 01-74 0z" fill="#e6e6e6" stroke="#ccc"/><ellipse cx="85" cy="60" rx="37" ry="10" fill="#f4f4f4" stroke="#ccc"/><ellipse cx="85" cy="102" rx="16" ry="6" fill="#999"/></svg></div>
<div class="abs pname" style="left:234px;top:2353px">Parkway Suspended</div>
<div class="abs pname" style="left:422px;top:2353px">Wardline</div>
<div class="abs pname" style="left:609px;top:2353px">Townline</div>
<div class="abs pname" style="left:797px;top:2353px">Airflow Downlight Overview</div>

<div class="abs" style="left:0;width:1200px;top:2422px;text-align:center"><span class="plus-link">+ VIEW ALL PRODUCTS</span></div>

<!-- subscribe -->
<section class="abs subscribe">
  <h3 class="abs">Subscribe to News and Updates</h3>
  <div class="abs field">Enter your email address</div>
  <div class="abs btn-dark">SUBSCRIBE</div>
</section>

<!-- footer -->
<footer class="abs footer">
  <div class="abs fcol" style="left:234px">
    <h5>CONTACT INFO</h5>
    <div class="contact-line"><svg width="12" height="14" viewBox="0 0 24 28"><path d="M12 1a9 9 0 00-9 9c0 7 9 17 9 17s9-10 9-17a9 9 0 00-9-9z" fill="#222"/><circle cx="12" cy="10" r="3.5" fill="#f7f7f7"/></svg><span>4715 Street Name,<br>City, Country - Y123</span></div>
    <div class="contact-line"><svg width="12" height="12" viewBox="0 0 24 24"><path d="M6.6 10.8a15 15 0 006.6 6.6l2.2-2.2c.3-.3.7-.4 1-.2 1.1.4 2.3.6 3.6.6.6 0 1 .4 1 1V20c0 .6-.4 1-1 1C10.6 21 3 13.4 3 4c0-.6.4-1 1-1h3.5c.6 0 1 .4 1 1 0 1.3.2 2.5.6 3.6.1.3 0 .7-.2 1z" fill="#222"/></svg><span>000-123-4567</span></div>
    <div class="contact-line"><svg width="12" height="10" viewBox="0 0 24 18"><rect x="1" y="1" width="22" height="16" fill="#222"/><path d="M1 1l11 9 11-9" fill="none" stroke="#f7f7f7" stroke-width="1.6"/></svg><span>info@companyname.com</span></div>
  </div>
  <div class="abs fcol" style="left:429px">
    <h5>QUICK LINKS</h5>
    <div style="display:flex;gap:50px"><ul><li>Products</li><li>Solutions</li><li>Case Studies</li><li>Downloads</li></ul><ul><li>About Us</li><li>Blog</li><li>FAQ</li><li>Contact Us</li></ul></div>
  </div>
  <div class="abs fcol" style="left:635px"><h5>INFORMATION</h5><ul><li>Search Terms</li><li>Advanced Search</li><li>Help &amp; Faq's</li><li>Careers</li></ul></div>
  <div class="abs fcol" style="left:790px"><h5>USEFUL LINKS</h5><ul><li>Privacy Policy</li><li>Returns</li><li>Terms &amp; Conditions</li><li>Sitemap</li></ul></div>

  <div class="abs reviews" style="left:242px;top:207px;font-weight:600;font-size:8.5px">LIGHTING COMPANY REVIEWS</div>
  <div class="abs reviews" style="left:386px">OVERALL RATING / 16 TOTAL 1ST-PARTY REVIEWS<br>
    <span class="stars">★★★★★</span> <span style="font-size:12px">5.0</span> OUT OF 5 STARS &nbsp;&nbsp;<span style="text-decoration:underline">VIEW REVIEWS</span></div>
  <div class="abs reviews" style="left:665px;top:205px;font-weight:600">FOLLOW US ON SOCIAL MEDIA</div>
  <div class="abs social" style="left:664px"><i></i><i></i><i></i><i></i><i></i></div>
</footer>
<div class="abs base">Copyright © 2019 Lighting.&nbsp; All Rights Reserved</div>

</body>
</html>
```